KRV Business Cards

We are a local commercial development company based in Silicon Valley and we would like a new business card. I've attached a copy of our company brochure to give a flavor of what we do, our logo, info company colors/graphics, and our current business card. We don't necessarily need a crazy makeover, but would like something that feels a little bit more "fresh" and modern (we've had the same business card design for 15+ years), but still in keeping with our overall brand -- clean, high-quality, modern but timeless. Would like to add our website to the info on the card (www.velmara.com) and would like the flexibility for some folks to have an efax number listed and some not to have that included (without it looking like there is a hole).

```html
<!DOCTYPE html>
<html lang="en">
<head>
<meta charset="utf-8">
<title>KRV Business Cards</title>
<link href="https://fonts.googleapis.com/css2?family=Cinzel:wght@400;500&family=Jost:wght@400&family=Roboto:wght@400&display=swap" rel="stylesheet">
<style>
  :root {
    --backdrop: #2b2b2b;
    --brand-blue: #38526b;
    --paper: #f2f2f2;
    --ink-light: #ffffff;
    --ink-dark: #444444;
  }
  html, body {
    margin: 0;
    width: 1200px;
    height: 960px;
    overflow: hidden;
    background: var(--backdrop);
  }
  .canvas { position: relative; width: 1200px; height: 960px; }
  .card {
    position: absolute;
    width: 600px;
    height: 342px;
    box-shadow: 0 3px 8px rgba(0,0,0,.45);
  }
  .card-front { left: 314px; top: 113px; background: var(--brand-blue); color: var(--ink-light); }
  .card-back { left: 311px; top: 472px; background: var(--paper); }

  .brand-name {
    position: absolute;
    display: flex;
    align-items: center;
    gap: 12px;
    margin: 0;
    font-family: "Jost", sans-serif;
    font-weight: 400;
    font-size: 26px;
    line-height: 30px;
    letter-spacing: 5px;
    color: var(--ink-light);
  }
  .brand-name .brand-square {
    width: 12px; height: 12px;
    background: var(--ink-light);
    flex: none;
  }
  .card-front .brand-name { left: 76px; top: 156px; }

  .divider {
    position: absolute;
    left: 310px; top: 62px;
    width: 2px; height: 220px;
    background: linear-gradient(to bottom, rgba(255,255,255,0), rgba(255,255,255,.9) 50%, rgba(255,255,255,0));
  }

  .contact { position: absolute; left: 342px; top: 74px; }
  .person-name {
    font-family: "Cinzel", serif;
    font-weight: 500;
    font-size: 21px;
    line-height: 24px;
    margin: 0;
    letter-spacing: .5px;
  }
  .person-title {
    font-family: "Cinzel", serif;
    font-weight: 500;
    font-size: 15px;
    line-height: 18px;
    margin: 0 0 12px;
    letter-spacing: .5px;
  }
  .address, .lines {
    font-family: "Jost", sans-serif;
    font-size: 15.5px;
    line-height: 19.3px;
    margin: 0;
    list-style: none;
    padding: 0;
  }
  .address { margin-bottom: 5px; }
  .lines li { display: flex; align-items: center; gap: 8px; }
  .lines svg { width: 14px; height: 14px; fill: var(--ink-light); flex: none; }

  .logo-panel {
    position: absolute;
    left: 169px; top: 100px;
    width: 262px; height: 141px;
    background: var(--brand-blue);
    display: flex;
    align-items: center;
    justify-content: center;
  }
  .logo-panel .brand-name { position: static; }
  .web-address {
    position: absolute;
    left: 0; right: 0; top: 292px;
    text-align: center;
    font-family: "Roboto", sans-serif;
    font-size: 15px;
    letter-spacing: 8.5px;
    color: var(--ink-dark);
    margin: 0;
  }
</style>
</head>
<body>
<div class="canvas">
  <section class="card card-front">
    <p class="brand-name"><span class="brand-square"></span>VELMARA</p>
    <div class="divider"></div>
    <div class="contact">
      <p class="person-name">Nora J. Halvorsen</p>
      <p class="person-title">Partner</p>
      <p class="address">212 Linden Court<br>Mountain View, California 94041</p>
      <ul class="lines">
        <li><svg viewBox="0 0 24 24" aria-hidden="true"><path d="M6.6 10.8a15.1 15.1 0 0 0 6.6 6.6l2.2-2.2c.3-.3.7-.4 1-.2 1.1.4 2.3.6 3.6.6.6 0 1 .4 1 1V20c0 .6-.4 1-1 1A17 17 0 0 1 3 4c0-.6.4-1 1-1h3.5c.6 0 1 .4 1 1 0 1.3.2 2.5.6 3.6.1.3 0 .7-.2 1z"/></svg>555.214.0386</li>
        <li><svg viewBox="0 0 24 24" aria-hidden="true"><path d="M6.6 10.8a15.1 15.1 0 0 0 6.6 6.6l2.2-2.2c.3-.3.7-.4 1-.2 1.1.4 2.3.6 3.6.6.6 0 1 .4 1 1V20c0 .6-.4 1-1 1A17 17 0 0 1 3 4c0-.6.4-1 1-1h3.5c.6 0 1 .4 1 1 0 1.3.2 2.5.6 3.6.1.3 0 .7-.2 1z"/></svg>555.214.0100 (main)</li>
        <li><svg viewBox="0 0 24 24" aria-hidden="true"><path d="M6 2h12v6H6zM3 9h18v9h-3v4H6v-4H3zm5 7v4h8v-4z"/></svg>555.219.4471</li>
        <li><svg viewBox="0 0 24 24" aria-hidden="true"><path d="M2 5h20v14H2zm2 2v.5l8 5 8-5V7z"/></svg>nora@velmara.com</li>
        <li><svg viewBox="0 0 24 24" aria-hidden="true"><path d="M12 2a10 10 0 1 0 0 20 10 10 0 0 0 0-20zm-1 17.9A8 8 0 0 1 4.1 10L9 15v1c0 1.1.9 2 2 2zm6.9-2.5A2 2 0 0 0 16 16h-1v-3c0-.6-.4-1-1-1H8v-2h2c.6 0 1-.4 1-1V7h2c1.1 0 2-.9 2-2v-.4a8 8 0 0 1 2.9 12.8z"/></svg>www.velmara.com</li>
      </ul>
    </div>
  </section>

  <section class="card card-back">
    <div class="logo-panel">
      <p class="brand-name"><span class="brand-square"></span>VELMARA</p>
    </div>
    <p class="web-address">www.velmara.com</p>
  </section>
</div>
</body>
</html>
```